Graphic Design for our Dromer Vans

Creative Vehicle Branding & Van Wrap Design – RFP
Corvane Fieldworks Inc. (CFI) is seeking a creative, innovative designer or agency to develop a new, standout branding design for our four Brenvik Dromer service vans.
This design must reflect who we are and what we do: electrical service, construction, and large-scale commercial, roadway, and sports lighting. This is a company that works in the air, not behind a desk.
The Objective
Create a highly recognizable, eye-catching van design that:
Clearly communicates electrical and lighting expertise
Reflects scale, capability, and professionalism
Stands out on highways, job sites, and parking lots
Feels bold and modern, not generic contractor stock art
Our vans are rolling billboards for serious infrastructure work. They should look the part.
Critical Context (Read This Carefully)
Most of our work is performed from bucket trucks
We operate bucket trucks reaching up to 140 feet
Our crews work on:
Street and roadway lighting
Sports field lighting
Commercial and industrial lighting
Electrical service and construction
The design should acknowledge verticality, height, light, and scale.
That could mean visual elements that imply:
Reaching upward
Light projection
Infrastructure
Power, precision, and access
Literal illustrations are not required, but the design should feel relevant to high-reach, high-visibility work.
Non-Negotiables
The existing CFI logo stays exactly as-is
No redesigns, distortions, or reinterpretations of the logo
Everything else is open for exploration
Creative Freedom (Encouraged)
You may explore:
Bold color systems
High-contrast layouts
Clean, strong typography (outside the logo)
Abstract or graphic representations of light, elevation, or power
Minimal but impactful messaging
If it looks like every other electrical contractor van, we’re not interested.
Design Requirements
Eye-catching at speed and from distance
Clean and professional up close
Scalable across four vans and future fleet growth
Practical for real-world wrap production
Timeless enough to last, modern enough to matter
Scope of Work
Concept development (multiple design directions preferred)
Final wrap-ready design files for Brenvik Dromer vans
Layout consideration for sides, rear, and doors
Coordination-friendly designs for professional wrap installation
Who Should Respond
Designers or agencies with vehicle wrap or large-format branding experience
Strong conceptual thinkers who design with intent
Comfortable working with construction, electrical, or infrastructure brands
Willing to push ideas and explain the reasoning behind them
How to Respond
Please include:
Relevant portfolio examples (vehicle wraps strongly preferred)
Your creative approach and thinking process
Estimated timeline
Pricing structure
Any early concepts or ideas (optional but welcome)
We’re looking for a design that reflects scale, capability, and confidence.
This should look like a company that works at 140 feet in the air and knows exactly what it’s doing.

```html
<!DOCTYPE html>
<html lang="en">
<head>
<meta charset="utf-8">
<title>Corvane Fieldworks Inc. – Dromer Van Wrap</title>
<link rel="stylesheet" href="https://fonts.googleapis.com/css2?family=Oswald:wght@500;700&family=Roboto+Condensed:wght@700&family=Poppins:wght@500;600&display=swap">
<style>
  :root {
    --wrap-blue: #1f2a8c;
    --wrap-red: #c8102e;
    --wrap-white: #ffffff;
    --band-dark: #2b2b2d;
    --glass: #2f3238;
    --glass-light: #5a5f68;
    --tyre: #1a1a1a;
    --rim: #c4c6ca;
    --hub: #5b5e63;
    --seam: #c9c9c9;
    --lamp: #e07a2a;
    --page: #ffffff;
    --art-blue: #c9cfe9;
    --art-red: #f1c4cb;
  }
  html, body { margin: 0; padding: 0; overflow: hidden; background: var(--page); }
  .canvas { width: 1200px; height: 1200px; display: block; }
  .brand-name { font-family: "Oswald", sans-serif; font-weight: 700; fill: var(--wrap-red); }
  .brand-sub { font-family: "Oswald", sans-serif; font-weight: 700; fill: var(--wrap-blue); }
  .service-line { font-family: "Roboto Condensed", sans-serif; font-weight: 700; fill: var(--wrap-blue); }
  .service-line--light { fill: var(--wrap-white); }
  .sector-line { font-family: "Roboto Condensed", sans-serif; font-weight: 700; fill: var(--wrap-red); }
  .call-label { font-family: "Poppins", sans-serif; font-weight: 600; fill: var(--wrap-red); }
  .phone { font-family: "Poppins", sans-serif; font-weight: 600; fill: var(--wrap-blue); }
  .phone--light { fill: var(--wrap-white); }
  .web { font-family: "Poppins", sans-serif; font-weight: 500; fill: var(--wrap-white); letter-spacing: 1px; }
  .emergency { font-family: "Poppins", sans-serif; font-weight: 600; fill: var(--wrap-white); font-style: italic; }
  .unit-no { font-family: "Roboto Condensed", sans-serif; font-weight: 700; fill: var(--wrap-red); }
  .body-shell { fill: var(--wrap-white); stroke: #bdbdbd; stroke-width: 1.5; }
  .seam { stroke: var(--seam); stroke-width: 1.5; fill: none; }
</style>
</head>
<body>
<svg class="canvas" viewBox="0 0 1200 1200" xmlns="http://www.w3.org/2000/svg">
  <defs>
    <clipPath id="side-body-clip">
      <path d="M125 330 L120 255 Q122 215 145 200 L235 170 Q290 90 340 50 Q360 40 400 38 L1025 36 Q1068 38 1070 85 L1072 330 Z"/>
    </clipPath>

    <g id="side-shell">
      <path class="body-shell" d="M125 330 L120 255 Q122 215 145 200 L235 170 Q290 90 340 50 Q360 40 400 38 L1025 36 Q1068 38 1070 85 L1072 330 Z"/>
    </g>

    <g id="side-details">
      <g clip-path="url(#side-body-clip)">
        <rect x="110" y="275" width="970" height="60" fill="var(--band-dark)"/>
      </g>
      <rect x="362" y="312" width="408" height="16" fill="var(--wrap-red)"/>
      <path d="M112 258 L160 258 L160 336 L118 336 Q110 336 110 326 Z" fill="var(--band-dark)"/>
      <rect x="900" y="330" width="175" height="14" rx="6" fill="var(--band-dark)"/>
      <path d="M290 195 L345 88 Q352 78 366 77 L478 72 L478 195 Z" fill="var(--glass)"/>
      <path d="M240 172 L330 58 L346 52 L282 180 Z" fill="var(--glass-light)"/>
      <rect x="286" y="158" width="20" height="34" rx="5" fill="var(--glass)"/>
      <path d="M126 222 Q142 204 178 198 L182 216 Q150 226 128 240 Z" fill="var(--glass)"/>
      <path d="M150 214 L176 206 L178 214 L154 220 Z" fill="var(--lamp)"/>
      <rect x="1052" y="140" width="18" height="110" rx="4" fill="var(--wrap-red)"/>
      <line class="seam" x1="500" y1="40" x2="500" y2="275"/>
      <line class="seam" x1="762" y1="37" x2="762" y2="275"/>
      <rect x="425" y="208" width="34" height="8" rx="4" fill="#9a9a9a"/>
      <g class="wheel">
        <circle cx="278" cy="345" r="62" fill="#3a3a3a"/>
        <circle cx="278" cy="345" r="54" fill="var(--tyre)"/>
        <circle cx="278" cy="345" r="33" fill="var(--rim)"/>
        <circle cx="278" cy="345" r="12" fill="var(--hub)"/>
      </g>
      <g class="wheel">
        <circle cx="862" cy="345" r="62" fill="#3a3a3a"/>
        <circle cx="862" cy="345" r="54" fill="var(--tyre)"/>
        <circle cx="862" cy="345" r="33" fill="var(--rim)"/>
        <circle cx="862" cy="345" r="12" fill="var(--hub)"/>
      </g>
    </g>

    <g id="side-copy">
      <rect x="232" y="222" width="40" height="26" rx="4" fill="var(--wrap-white)" stroke="var(--wrap-blue)" stroke-width="2"/>
      <text class="unit-no" x="252" y="242" font-size="18" text-anchor="middle">001</text>
      <text class="call-label" x="322" y="225" font-size="17">Call Now!</text>
      <text class="phone" x="320" y="250" font-size="23">800-555-0142</text>
      <text class="service-line" x="632" y="62" font-size="14" text-anchor="middle">Electrical • Lighting • Sign Service</text>
      <text class="brand-name" x="632" y="112" font-size="44" text-anchor="middle">CORVANE</text>
      <text class="brand-name" x="632" y="157" font-size="44" text-anchor="middle">FIELDWORKS</text>
      <text class="brand-sub" x="632" y="180" font-size="18" text-anchor="middle">INCORPORATED</text>
      <text class="sector-line" x="632" y="214" font-size="15" text-anchor="middle">COMMERCIAL | GOVERNMENT</text>
      <text class="service-line" x="632" y="237" font-size="13" text-anchor="middle">• ROADWAY LIGHTING • SPORTS LIGHTING</text>
      <text class="service-line" x="632" y="255" font-size="13" text-anchor="middle">• COMMERCIAL LIGHTING • SIGNS • ELECTRICAL</text>
      <text class="web" x="565" y="298" font-size="18" text-anchor="middle">www.CorvaneFieldworks.com</text>
      <text class="emergency" x="905" y="78" font-size="15" text-anchor="middle">Emergency Services 24/7</text>
    </g>
  </defs>

  <!-- Side wrap, blue direction -->
  <g class="side-wrap side-wrap--blue">
    <use href="#side-shell"/>
    <g clip-path="url(#side-body-clip)">
      <path d="M765 30 Q790 160 762 280 L1080 280 L1080 30 Z" fill="var(--wrap-blue)"/>
    </g>
    <use href="#side-details"/>
    <rect x="795" y="96" width="240" height="166" rx="8" fill="var(--art-blue)" role="img" aria-label="Line illustration of a bucket truck with raised boom beside a street light"/>
    <use href="#side-copy"/>
  </g>

  <!-- Side wrap, red direction -->
  <g class="side-wrap side-wrap--red" transform="translate(0 405)">
    <use href="#side-shell"/>
    <g clip-path="url(#side-body-clip)">
      <path d="M765 30 Q790 160 762 280 L1080 280 L1080 30 Z" fill="var(--wrap-red)"/>
    </g>
    <use href="#side-details"/>
    <rect x="795" y="96" width="240" height="166" rx="8" fill="var(--art-red)" role="img" aria-label="Line illustration of a bucket truck with raised boom beside a street light"/>
    <use href="#side-copy"/>
  </g>

  <!-- Front view -->
  <g class="front-wrap">
    <rect x="176" y="918" width="48" height="52" rx="8" fill="var(--glass)"/>
    <rect x="516" y="918" width="48" height="52" rx="8" fill="var(--glass)"/>
    <path class="body-shell" d="M230 1100 L222 900 Q226 862 260 858 L480 858 Q514 862 518 900 L510 1100 Z"/>
    <path d="M252 948 L262 882 Q266 870 280 870 L460 870 Q474 870 478 882 L488 948 Z" fill="var(--glass)"/>
    <text class="brand-name" x="370" y="975" font-size="19" text-anchor="middle">CORVANE FIELDWORKS</text>
    <text class="brand-sub" x="370" y="989" font-size="9" text-anchor="middle">INCORPORATED</text>
    <path d="M232 996 L278 996 L276 1016 L236 1020 Z" fill="#d7d9dc" stroke="#8a8a8a"/>
    <path d="M508 996 L462 996 L464 1016 L504 1020 Z" fill="#d7d9dc" stroke="#8a8a8a"/>
    <rect x="284" y="996" width="172" height="60" rx="10" fill="var(--band-dark)"/>
    <line x1="294" y1="1012" x2="446" y2="1012" stroke="#9a9a9a" stroke-width="3"/>
    <line x1="294" y1="1026" x2="446" y2="1026" stroke="#9a9a9a" stroke-width="3"/>
    <line x1="294" y1="1040" x2="446" y2="1040" stroke="#9a9a9a" stroke-width="3"/>
    <rect x="214" y="1064" width="312" height="58" rx="14" fill="var(--band-dark)"/>
    <rect x="222" y="1118" width="44" height="34" rx="6" fill="var(--tyre)"/>
    <rect x="474" y="1118" width="44" height="34" rx="6" fill="var(--tyre)"/>
  </g>

  <!-- Rear view -->
  <g class="rear-wrap">
    <path class="body-shell" d="M668 1095 L666 900 Q668 858 710 856 L930 856 Q972 858 974 900 L972 1095 Z"/>
    <rect x="690" y="860" width="260" height="20" rx="8" fill="var(--wrap-blue)"/>
    <text class="web" x="820" y="875" font-size="11" text-anchor="middle">www.CorvaneFieldworks.com</text>
    <text class="brand-name" x="820" y="912" font-size="26" text-anchor="middle">CORVANE</text>
    <text class="brand-name" x="820" y="940" font-size="26" text-anchor="middle">FIELDWORKS</text>
    <text class="brand-sub" x="820" y="958" font-size="12" text-anchor="middle">INCORPORATED</text>
    <text class="call-label" x="697" y="980" font-size="8">Call Now! 24/7 service line</text>
    <rect x="667" y="985" width="306" height="20" fill="var(--wrap-blue)"/>
    <rect x="667" y="1005" width="306" height="52" fill="var(--wrap-red)"/>
    <text class="phone phone--light" x="697" y="1001" font-size="15">800-555-0142</text>
    <text class="service-line service-line--light" x="697" y="1024" font-size="8">ROADWAY LIGHTING  SPORTS LIGHTING</text>
    <text class="service-line service-line--light" x="697" y="1036" font-size="8">COMMERCIAL LIGHTING  SIGNS  ELECTRICAL</text>
    <rect x="856" y="975" width="100" height="70" rx="6" fill="var(--art-blue)" role="img" aria-label="Small illustration of a bucket truck reaching a street light"/>
    <line class="seam" x1="820" y1="1057" x2="820" y2="1092"/>
    <rect x="668" y="950" width="14" height="100" rx="4" fill="var(--wrap-red)"/>
    <rect x="958" y="950" width="14" height="100" rx="4" fill="var(--wrap-red)"/>
    <rect x="678" y="1092" width="284" height="42" rx="12" fill="var(--band-dark)"/>
    <rect x="785" y="1100" width="70" height="22" rx="3" fill="#55585e"/>
    <rect x="690" y="1128" width="42" height="30" rx="6" fill="var(--tyre)"/>
    <rect x="908" y="1128" width="42" height="30" rx="6" fill="var(--tyre)"/>
  </g>
</svg>
</body>
</html>
```